Personal coach needs brochure design for inspirational essay about authenticity

Overview:
I want a beautiful brochure, 11”x17” that folds to 8-1/2”x11” with 4 pages. Think of it as an oversize greeting card.
• Front cover: photograph of a dancer and title with attribution of quote (Lumafold jpeg photo attached)
• Inside spread: Copy (Helena Brisk copy attached) with some appropriate illustration, based on cover photo
• Back cover: contact information, brief descriptive copy, two small photos (jpeg photo attached; see copy for direction)
Copy for front cover title, inside spread and back cover is attached in doc titled "Helena Brisk copy"

Purpose of brochure:
I'm a personal coach and once a year I produce a 4-page illustrated inspirational essay, which invites personal reflection on living a more mindful, meaningful life. Most people I send them to collect them. Someday in the future I'd like to put a collection of these essays into a coffee table book and also create a website for the collection, which is related to the personal coaching that I do.
I have the brochures printed hard copy. I have attached a few examples from previous years. Each has a unique design related to its theme.

Concept:
This year’s essay theme, “There will only ever be one you!” is based on a quote by Helena Brisk, a famous modern dancer. The complete quote, which appears in the copy, is about being true to one’s authentic self. The essay is not about dance, but because the author of the quote was a dancer who personified this theme of being unique to self, I have selected a photo of dance for the cover.

Design Guidance:
Front cover: One possibility is to expand the background color of the Lumafold photo so the photo seems to emerge from the background. But I am open to ideas. I think the photo is artsy enough as it is, but there may be other ways to treat it (e.g. special effects) that would also work. The title should appear somewhere. Make the attribution (--Helena Brisk) in smaller type than the title.

Inside Spread: There may be ways to borrow a design motif from the cover photo to make the inside spread more visually interesting, i.e., not just straight copy. I think it may be helpful to make the font size of the quote larger than the rest of the copy, but it has to be read in sequence. Or maybe it's printed in same size as copy, but then also repeated and displayed by itself in larger type.

Back cover: If you look at some of the other examples I’ve sent, you’ll see how the back cover is typically handled. I want a reduced version of the cover to be placed near the line that says "this is the 16th in a series.." Then, there’s a jpeg photo of Helena Brisk that should be placed next to the copy description of her.

Need extra days to review

```html
<!DOCTYPE html>
<html lang="en">
<head>
<meta charset="utf-8">
<title>There Will Only Ever Be One You – Brochure Outer Spread</title>
<link rel="stylesheet" href="https://fonts.googleapis.com/css2?family=DM+Sans:wght@300;400&family=Playfair+Display:ital,wght@0,700;1,400;1,700&display=swap">
<style>
  :root {
    --violet-light: #4b3d7a;
    --violet-deep: #382c5a;
    --cream: #f7f3e3;
    --orchid: #df98c8;
    --orchid-soft: #d7aed6;
    --paper: #f2eef6;
    --caption: #a79cb8;
    --photo-dark: #2b2630;
    --photo-mid: #6e6878;
  }
  * { margin: 0; padding: 0; box-sizing: border-box; }
  html, body { width: 1200px; height: 776px; overflow: hidden; background: var(--violet-deep); }
  .spread {
    position: relative; width: 1200px; height: 776px;
    background: var(--violet-deep);
    font-family: "DM Sans", sans-serif; font-weight: 300;
  }
  .back-band {
    position: absolute; left: 0; top: 0; width: 600px; height: 254px;
    background: var(--violet-light);
  }
  .series-note {
    position: absolute; left: 42px; top: 38px; width: 320px;
    color: var(--paper); font-size: 12px; line-height: 14.2px; font-weight: 400;
  }
  .series-note em {
    font-family: "Playfair Display", serif; font-style: italic; color: var(--orchid);
  }
  .contact {
    position: absolute; left: 42px; top: 103px;
    color: var(--paper); font-size: 10px; line-height: 11.8px;
  }
  .contact p + p { margin-top: 11px; }
  .copyright { position: absolute; left: 42px; top: 207px; color: var(--paper); font-size: 10px; }
  .cover-thumb {
    position: absolute; left: 413px; top: 42px; width: 147px; height: 145px;
    border: 1px solid var(--orchid); border-radius: 3px; padding: 3px;
  }
  .cover-thumb .photo { width: 100%; height: 100%; border-radius: 2px; }
  .photo {
    background: radial-gradient(ellipse at 55% 45%, var(--photo-mid) 0%, #4c4654 45%, var(--photo-dark) 100%);
  }
  .portrait {
    position: absolute; left: 43px; top: 315px; width: 185px; height: 163px;
    background: radial-gradient(ellipse at 45% 55%, #8f887e 0%, #3a3436 40%, #1c1719 100%);
  }
  .portrait-caption {
    position: absolute; left: 41px; top: 482px;
    color: var(--caption); font-size: 8.5px; line-height: 11px;
  }
  .section-title {
    font-family: "Playfair Display", serif; font-style: italic; font-weight: 400;
    color: var(--paper); font-size: 13px;
  }
  .section-body {
    color: var(--orchid-soft); font-size: 10px; line-height: 11.8px; margin-top: 15px;
  }
  .about-dancer { position: absolute; left: 239px; top: 314px; width: 324px; }
  .about-photographer { position: absolute; left: 43px; top: 533px; width: 322px; }
  .heart { position: absolute; left: 460px; top: 656px; width: 99px; height: 86px; }
  .cover-photo {
    position: absolute; left: 600px; top: 0; width: 600px; height: 400px;
  }
  .cover-title {
    position: absolute; left: 656px; top: 322px;
    font-family: "Playfair Display", serif; font-weight: 700;
    color: var(--cream); font-size: 84px; line-height: 80px; letter-spacing: -0.5px;
  }
  .cover-title .accent { font-style: italic; color: var(--orchid); }
  .attribution {
    position: absolute; left: 658px; top: 666px;
    color: var(--orchid); font-size: 18.5px; font-weight: 400; letter-spacing: 0.3px;
  }
</style>
</head>
<body>
<main class="spread">
  <section class="back-cover">
    <div class="back-band"></div>
    <p class="series-note"><em>There Will Only Ever Be One You</em> is the 16th in a series of Labor Day essays inviting a moment of reflection on living a more meaningful, more mindful life.</p>
    <div class="contact">
      <p>Nora Vell Asher, Ph.D.<br>Heron Hill House<br>18 Orchard Lane<br>Millbrook, Vermont&nbsp; 05999</p>
      <p>Mobile:&nbsp; 555-013-2846<br>Email: nvasher@mailbox.example</p>
    </div>
    <p class="copyright">©2023</p>
    <div class="cover-thumb"><div class="photo" role="img" aria-label="Reduced cover photo of a leaping dancer in a flowing dark dress amid drifting dust"></div></div>
  </section>

  <section class="inside-notes">
    <div class="portrait" role="img" aria-label="Black and white photograph of a dancer in a swirling white gown"></div>
    <p class="portrait-caption">“Helena Brisk in Letter to the World, No. 1”<br>© The Clara Winslow Archive</p>

    <article class="about-dancer">
      <h2 class="section-title">About Helena Brisk:</h2>
      <p class="section-body">Born in 1894, Helena Brisk danced and taught for over 70 years. She is recognized as a primal artistic force of the 20th century, whose influence on modernity has been compared to Renzo Alvar, Tomas Hale, Ivo Marren, and Elias Crane Ford.&nbsp; Her themes dealt with the lives and conflicts of ordinary people, and she brought serious issues to the stage like war, poverty, intolerance and the injustices of slavery and treatment of Native Americans. Rebelling against conventions of the past, her dancing and choreography exposed the depths of human emotion through intense movements that were forceful, stark, angular, jagged, and percussive – startlingly unlike the formality of classical ballet, which she saw as antiquated.</p>
    </article>

    <article class="about-photographer">
      <h2 class="section-title">About Photographer Clara Winslow:</h2>
      <p class="section-body">In 1935 Clara Winslow saw a performance by modern dancer and choreographer Helena Brisk. Winslow was so inspired by the dance performance that she introduced herself to Brisk, and the two artists began an artistic collaboration that lasted more than 60 years. Winslow often photographed dancers in action, to capture the emotion behind their movement. Her artistic style was in line with Brisk’s philosophy of dance. This photo from the dance, “Letter to the World,” is one of Winslow’s most famous photographs. The title of this work comes from an Ada Thornfield poem, which inspired Brisk to create a dance performance based on Thornfield’s life.</p>
    </article>

    <svg class="heart" viewBox="0 0 100 86" aria-hidden="true">
      <path d="M50 84 C30 66 3 50 3 26 C3 11 14 2 27 2 C38 2 46 9 50 18 C54 9 62 2 73 2 C86 2 97 11 97 26 C97 50 70 66 50 84 Z" fill="var(--orchid)"/>
    </svg>
  </section>

  <section class="front-cover">
    <div class="cover-photo photo" role="img" aria-label="Dancer leaping with arms raised in a flowing dark dress against a dusty grey background"></div>
    <h1 class="cover-title">There will<br>only ever<br>be one<br><span class="accent">you!</span></h1>
    <p class="attribution">– Helena&nbsp; Brisk</p>
  </section>
</main>
</body>
</html>
```